BFCM Creatives Theme

We are looking for an initial design for our BFCM campaign this year to set the theme for all other creatives for BFCM. We are an ecommerce brand selling Merino wool baby clothing. Our flagship product is the Cozyloft Infant Nap Pouch (see images).

We are starting with the request for an instagram post, announcing the sale (details below). This post should be 1080x1350 but also look appealing in the square grid. I've attached a basic brand card showing color palette, fonts, and logos. I will also attach some image options. We are looking for your creativity to shine while aligning with our branding and connecting with the customer. If you have a specific idea and are looking for a specific image please contact us.

Sale Details:
- 20% Off Sitewide
- 11.28.24 - 12.02.24
- Excluding giftcards and imperfects. No rainchecks.

```html
<!DOCTYPE html>
<html lang="en">
<head>
<meta charset="utf-8">
<title>lanabee – 20% Off Sitewide</title>
<link rel="stylesheet" href="https://fonts.googleapis.com/css2?family=Poppins:wght@200;300;400;500;700&family=Kalam:wght@700&display=swap">
<style>
  :root {
    --page: #ffffff;
    --panel-light: #f0efed;
    --panel-shade: #dfdcd6;
    --badge: #a8a497;
    --ink: #343434;
    --white: #ffffff;
    --gold: #c4a548;
    --pink-light: #f8dcdf;
    --pink-mid: #f1c3c8;
    --skin: #f2c6a8;
  }
  * { margin: 0; padding: 0; box-sizing: border-box; }
  html, body { width: 1200px; height: 844px; overflow: hidden; background: var(--page); }
  body { position: relative; font-family: "Poppins", sans-serif; color: var(--ink); }

  .post { position: absolute; overflow: hidden; background: var(--panel-light); }
  .post--portrait { left: 72px; top: 109px; width: 505px; height: 630px; }
  .post--square { left: 631px; top: 109px; width: 505px; height: 504px; }

  .post__backdrop, .post__swoosh { position: absolute; left: 0; top: 0; width: 100%; height: 100%; }

  .post__photo {
    position: absolute;
    background: linear-gradient(180deg, var(--skin) 0%, var(--skin) 22%, var(--pink-mid) 30%, var(--pink-light) 65%, var(--pink-mid) 100%);
    border-radius: 46% 46% 40% 40% / 22% 22% 14% 14%;
  }
  .post--portrait .post__photo { left: 30px; top: 22px; width: 300px; height: 598px; }
  .post--square .post__photo { left: 18px; top: 8px; width: 280px; height: 520px; }

  .brand { position: absolute; display: flex; align-items: center; }
  .brand__dot { border-radius: 50%; border: 3px solid var(--ink); }
  .brand__name { font-weight: 500; letter-spacing: -0.5px; line-height: 1; }
  .post--portrait .brand { left: 243px; top: 41px; gap: 10px; }
  .post--portrait .brand__dot { width: 42px; height: 42px; }
  .post--portrait .brand__name { font-size: 42px; }
  .post--square .brand { left: 256px; top: 28px; gap: 9px; }
  .post--square .brand__dot { width: 36px; height: 36px; }
  .post--square .brand__name { font-size: 37px; }

  .badge {
    position: absolute; border-radius: 50%; background: var(--badge); color: var(--white);
    display: flex; flex-direction: column; align-items: center; justify-content: center; text-align: center;
  }
  .badge__value { font-weight: 700; line-height: 0.9; letter-spacing: -2px; }
  .badge__label { font-weight: 200; line-height: 0.95; }
  .post--portrait .badge { left: 243px; top: 102px; width: 224px; height: 224px; }
  .post--portrait .badge__value { font-size: 76px; margin-top: 4px; }
  .post--portrait .badge__label { font-size: 64px; }
  .post--square .badge { left: 265px; top: 81px; width: 182px; height: 182px; }
  .post--square .badge__value { font-size: 62px; margin-top: 4px; }
  .post--square .badge__label { font-size: 52px; }

  .headline {
    position: absolute; font-family: "Kalam", cursive; font-weight: 700; color: var(--ink);
    line-height: 1; letter-spacing: -1px; white-space: nowrap;
    transform: translate(-50%, -50%) rotate(-10deg);
  }
  .post--portrait .headline { left: 374px; top: 355px; font-size: 42px; }
  .post--square .headline { left: 356px; top: 294px; font-size: 37px; }

  .dates { position: absolute; text-align: center; font-weight: 300; letter-spacing: -1.5px; line-height: 1; }
  .dates__arrow { display: block; margin: 0 auto; }
  .post--portrait .dates { left: 334px; top: 406px; width: 120px; font-size: 28px; }
  .post--portrait .dates__arrow { width: 14px; height: 12px; margin: 6px auto 8px; }
  .post--square .dates { left: 322px; top: 341px; width: 108px; font-size: 24px; }
  .post--square .dates__arrow { width: 12px; height: 10px; margin: 5px auto 6px; }

  .terms { position: absolute; font-weight: 300; line-height: 1.3; white-space: nowrap; }
  .terms__mark { position: absolute; left: -11px; top: -4px; }
  .terms__gap { display: block; height: 4px; }
  .post--portrait .terms { left: 350px; top: 523px; font-size: 12px; }
  .post--square .terms { left: 340px; top: 428px; font-size: 10.5px; }
</style>
</head>
<body>

<section class="post post--portrait">
  <svg class="post__backdrop" viewBox="0 0 505 630" preserveAspectRatio="none" aria-hidden="true">
    <path d="M0 0 H505 V68 Q260 330 0 581 Z" fill="var(--panel-shade)"/>
  </svg>
  <div class="post__photo" role="img" aria-label="Smiling baby wearing a pink strawberry-print Cozyloft Infant Nap Pouch"></div>
  <div class="brand"><span class="brand__dot"></span><span class="brand__name">lanabee</span></div>
  <div class="badge"><span class="badge__value">20%</span><span class="badge__label">OFF</span></div>
  <svg class="post__swoosh" viewBox="0 0 505 630" aria-hidden="true">
    <path d="M294 403 Q380 372 487 362 Q385 376 294 403 Z" fill="var(--gold)" stroke="var(--gold)" stroke-width="1.5"/>
  </svg>
  <div class="headline">Sitewide</div>
  <div class="dates">
    <span>11.28.24</span>
    <svg class="dates__arrow" viewBox="0 0 14 12"><path d="M1 1 H13 L7 11 Z" fill="none" stroke="var(--ink)" stroke-width="1.2"/></svg>
    <span>12.02.24</span>
  </div>
  <p class="terms"><span class="terms__mark">*</span>Excluding giftcards<br>and imperfects.<span class="terms__gap"></span>No rainchecks.</p>
</section>

<section class="post post--square">
  <svg class="post__backdrop" viewBox="0 0 505 504" preserveAspectRatio="none" aria-hidden="true">
    <path d="M0 0 H503 Q420 250 0 491 Z" fill="var(--panel-shade)"/>
  </svg>
  <div class="post__photo" role="img" aria-label="Smiling baby wearing a pink strawberry-print Cozyloft Infant Nap Pouch"></div>
  <div class="brand"><span class="brand__dot"></span><span class="brand__name">lanabee</span></div>
  <div class="badge"><span class="badge__value">20%</span><span class="badge__label">OFF</span></div>
  <svg class="post__swoosh" viewBox="0 0 505 504" aria-hidden="true">
    <path d="M284 341 Q360 314 456 305 Q365 318 284 341 Z" fill="var(--gold)" stroke="var(--gold)" stroke-width="1.3"/>
  </svg>
  <div class="headline">Sitewide</div>
  <div class="dates">
    <span>11.28.24</span>
    <svg class="dates__arrow" viewBox="0 0 14 12"><path d="M1 1 H13 L7 11 Z" fill="none" stroke="var(--ink)" stroke-width="1.2"/></svg>
    <span>12.02.24</span>
  </div>
  <p class="terms"><span class="terms__mark">*</span>Excluding giftcards<br>and imperfects.<span class="terms__gap"></span>No rainchecks.</p>
</section>

</body>
</html>
```